Small Business Directory Site Requires a Professional Responsive Web Design

Small Business Directory and Coupon Site - we require a complete website design for a brand new responsive & mobile friendly website. We already have a coder who will professional code our website in Magento.

All PSD pages need to be professionally designed then uploaded into a sharedrive (i.e. like filemoor). Additionally, as I cannot pre-empt everything, please note that we may require a little more assistance once the files have been transferred (for example, in www.brambleleaf.com if you hover your mouse on the search box you will see a pop up box. We want one of these too and I think that means there may be extra design work here)

We have some draft page sketches have been created (there are some minor changes we want to the sketches provided though); however, we require an excellent designer to add the creative touches to it to make it look professionally created. All artwork/font must be legal.

-------------------------
We like the look of the www.brambleleaf.com and www. corvinlist.com

For the headers, please consider a font similar to TKV marigold. We likes this style, but it is too thin for the headers...so we need a variation like this one. For the copy/general text font, something basic that marries well with the headers.

---------------------

Please be sure to also read the brief we wrote for the coder as this will help with better understanding our design requirements.

In total I believe we have about 50 pages. This includes all the little pages and most of the pop up boxes (but not the little help key boxes). For example, pages include...

1. Login (this is where customers log in and can edit, manage their profiles. This means that there are backend membership pages)
2. Mini Services (same look and feel as the business coupons)
3. Resource Centre
4. Join (this is where customers learn about the packages available to submit a directory listing, if they ‘buy’ a package (i.e. free, $25 or $150 package) then they can create their own directory listing)
5. Search the directory (customer can view all the categories and also search the directory)
6. Create a directory listing (this is where customers learn about the packages available to submit a directory listing, if they ‘buy’ a package (i.e. free, $25 or $150 package) then they can create their own directory listing)
7. Quote finder (also know as Get a Quote)
8. Coupons (customer go to the business coupon page and can view all current coupons/submit a coupon)
9. Submit a coupon (form)
10.Advertise with us (form)
11. Join the forum
12.Submit an article or video (form)
13. Affiliates (listing of affiliates we currently have)
14. Become an affiliate (form)
15. Case studies (customer can view the case studies we have in the resource centre)
16. Help Guides (customer can view the help guides we have in the resource centre)
17. About Us
18 .Contact Us (form)
19. Terms & Condition
20. Privacy Policy
21. Supporting City Councils
22. Site Map
23. Forgot password / login details
24. Homepage
25. If we hover over a few areas (i.e. search box, location field) it pops up with more information.
etc etc etc. . . there are more pages.

Please see our filemoor link for the draft mock up pages that I have created so far.

https://www.filemoor.com/sh/qp71tkw4mzr8ab/XKLdWeNoVtQsFyGh2Ju5pcMRi

We are in a rush! We'd like to get the majority of the artwork completed by the end of the month. Minor fixes/tweaks can occur thereafter.

Target Market(s)

Small Businesses (employees 0 - 50) located throughout Australia

Industry/Entity Type

Business

Font styles to use
Sans Serif

Requirements
Must have
• Professional. Artwork must be legal (cannot be cut and paste or taken off other websites, must be legally purchased and used).Must look contemporary, fresh, modern.

Absolutely must be a responsive site!
Nice to have
• original work, original photos, original art.

like modern, fresh photos that demonstrate innovation, growth, small business, Australian scenery, stability, goals/passion.
Should not have
• cut and paste graphics, illegal graphics, not purchased graphics.

```html
<!DOCTYPE html>
<html lang="en">
<head>
<meta charset="utf-8">
<title>TB Ally Link — Small Business Directory</title>
<link href="https://fonts.googleapis.com/css2?family=Questrial&family=Lato:wght@400;700&display=swap" rel="stylesheet">
<style>
:root{
  --orange:#f7891f;
  --orange-deep:#e8700f;
  --ink:#3a3a3a;
  --muted:#5b5b5b;
  --black:#000;
  --footer-bar:#232323;
  --white:#fff;
  --panel:rgba(70,40,10,.62);
  --heading-font:"Questrial",sans-serif;
  --body-font:"Lato",sans-serif;
}
*{box-sizing:border-box;margin:0;padding:0}
html,body{width:918px;height:1200px;overflow:hidden;background:var(--white)}
body{position:relative;font-family:var(--body-font);color:var(--ink)}
.abs{position:absolute}

/* hero */
.hero{left:0;top:0;width:918px;height:446px;overflow:hidden}
.hero-scene{position:absolute;inset:0;background:
  radial-gradient(ellipse 160px 60px at 430px 270px,#fff4b0 0%,#ffd23a 35%,rgba(255,170,20,0) 100%),
  linear-gradient(180deg,#e07a12 0%,#f3a21f 30%,#ffcc3a 52%,#e8901a 62%,#c9731a 100%)}
.brand{left:98px;top:0;width:234px;height:81px;background:var(--black);display:flex;align-items:center;gap:10px;padding-left:14px}
.brand-mark{width:16px;height:16px;background:var(--orange)}
.brand-name{font-family:var(--heading-font);font-size:19px;color:var(--white)}
.nav{left:381px;top:35px;display:flex;font-family:var(--heading-font);font-size:11.5px;color:var(--white)}
.nav span{padding:0 12px;border-left:1px solid rgba(255,255,255,.7);line-height:14px}
.nav span:first-child{border-left:0;padding-left:0}
.headline{left:98px;top:184px;font-family:var(--heading-font);font-size:31px;color:var(--white)}
.subline{left:98px;top:224px;font-family:var(--heading-font);font-size:17.5px;color:var(--white)}
.search{left:98px;top:255px;width:372px;height:49px;background:var(--orange)}
.field{top:14px;height:23px;background:var(--white);font-size:9px;color:#777;padding:7px 10px;border:1px solid #ddd}
.field.what{left:15px;width:159px}
.field.where{left:180px;width:151px}
.search-icon{left:337px;top:13px}
.dots{left:436px;top:425px;display:flex;gap:3px}
.dots i{width:10px;height:10px;border-radius:50%;background:var(--white);display:block}

.offer{left:607px;top:150px;width:214px;height:234px;background:var(--panel);border-radius:2px}
.offer-title{left:0;top:16px;width:214px;text-align:center;font-family:var(--heading-font);font-size:19px;line-height:22px;color:var(--white)}
.offer-card{left:34px;top:73px;width:145px;height:141px;background:var(--white);border:2px solid #ddd}
.price-band{left:30px;top:83px;width:152px;height:25px;background:#3b3b3b;display:flex;align-items:center;justify-content:center;gap:6px;color:var(--white);font-family:var(--heading-font);font-size:14px}
.price-band small{font-size:8px}
.tick{width:14px;height:14px;border-radius:50%;background:var(--orange);display:flex;align-items:center;justify-content:center}
.card-head{left:34px;top:120px;width:145px;text-align:center;font-size:8.5px;color:var(--orange-deep);font-weight:700}
.card-copy{left:42px;top:136px;width:129px;text-align:center;font-size:7px;line-height:12.8px;color:#666}
.pay-badge{left:83px;top:182px;width:42px;height:16px;border:1px solid #555;background:#f3f3f3}

/* community */
.section-title{left:0;top:476px;width:918px;text-align:center;font-family:var(--heading-font);font-size:24px;color:var(--ink)}
.col-head{text-align:center;font-family:var(--heading-font);font-size:16px;line-height:21px;color:var(--orange)}
.photo{border:1px solid #d6d6d6}
.copy{text-align:center;font-size:9.3px;line-height:15.6px;color:var(--muted)}
.btn{background:var(--orange);color:var(--white);font-family:var(--heading-font);font-size:10px;text-align:center;line-height:25px;border-radius:2px;box-shadow:0 2px 0 #c95e0a}
.affiliate-box{border:1px solid #ddd;display:flex;align-items:center;justify-content:center;gap:8px}
.affiliate-mark{width:22px;height:22px;background:#1f4f8a}
.affiliate-name{font-family:var(--heading-font);font-size:20px;color:#1f3d6b}

.partners{left:0;top:884px;width:918px;height:70px;border-top:1px solid #e4e4e4;display:flex;justify-content:space-around;align-items:center;padding:0 150px}
.partner{font-family:var(--heading-font);font-size:22px;color:#333}

/* footer */
.footer{left:0;top:954px;width:918px;height:200px;background:var(--black)}
.foot-col h4{font-family:var(--heading-font);font-weight:400;font-size:13px;color:var(--orange);margin-bottom:8px}
.foot-col li{list-style:none;font-size:9px;color:var(--white);line-height:17px}
.social{display:flex;gap:7px}
.social i{display:block;width:19px;height:19px;background:#3e6ea8;border-radius:2px}
.legal{left:0;top:1154px;width:918px;height:46px;background:var(--footer-bar)}
.legal p{position:absolute;left:107px;top:18px;font-size:9px;color:#888}
</style>
</head>
<body>

<header class="hero abs">
  <div class="hero-scene" role="img" aria-label="Sunset over a golden lake with birds flying across the sky"></div>
  <div class="brand abs"><span class="brand-mark"></span><span class="brand-name">TB Ally Link</span></div>
  <nav class="nav abs"><span>LOGIN</span><span>JOIN</span><span>FEATURE YOUR OFFER</span><span>GET A QUOTE</span><span>ADVERTISE</span></nav>
  <h1 class="headline abs" style="font-weight:400">It’s a Brand New Day.</h1>
  <p class="subline abs">Do More of What Your Love</p>
  <div class="search abs">
    <div class="field what abs">What are you looking for?</div>
    <div class="field where abs">Where?</div>
    <svg class="search-icon abs" width="22" height="22" viewBox="0 0 22 22"><circle cx="9" cy="9" r="6.5" fill="none" stroke="#fff" stroke-width="2.2"/><line x1="14" y1="14" x2="19" y2="19" stroke="#fff" stroke-width="2.6" stroke-linecap="round"/></svg>
  </div>
  <div class="offer abs">
    <div class="offer-title abs">Create a Directory<br>listing today</div>
    <div class="offer-card abs"></div>
    <div class="price-band abs"><span class="tick"><svg width="8" height="8" viewBox="0 0 8 8"><path d="M1 4l2 2 4-5" fill="none" stroke="#fff" stroke-width="1.5"/></svg></span>A $25/<small>YEAR</small></div>
    <div class="card-head abs">3 CATEGORY LISTING</div>
    <div class="card-copy abs">Lorem ipsum dolor sit amet consectetuer adipiscing elit Nam cursus Morbi</div>
    <div class="pay-badge abs"></div>
  </div>
  <div class="dots abs"><i></i><i></i><i></i><i></i></div>
</header>

<main>
  <h2 class="section-title abs" style="font-weight:400">Get Real Support from Our Community</h2>

  <h3 class="col-head abs" style="left:112px;top:550px;width:220px;font-weight:400">How Did You Sort<br>Your Business?</h3>
  <div class="photo abs" style="left:114px;top:600px;width:218px;height:122px;background:linear-gradient(135deg,#f4f5f7,#d9dde3 60%,#b8c6d6)" role="img" aria-label="Hands working with a tablet and charts on a desk"></div>
  <p class="copy abs" style="left:118px;top:731px;width:210px">Text: Learn from Dana Morrow, a real small business owner. How she started her business and what are the valuable resources for her right now.</p>
  <div class="btn abs" style="left:178px;top:814px;width:88px">CASE STUDY</div>

  <h3 class="col-head abs" style="left:362px;top:550px;width:220px;font-weight:400">Why Go with<br>TB Ally Link?</h3>
  <div class="photo abs" style="left:365px;top:600px;width:213px;height:122px;background:linear-gradient(120deg,#e7edf2,#c9d3dc 50%,#2c4670)" role="img" aria-label="Video still of two colleagues discussing work at a laptop"></div>
  <svg class="abs" style="left:455px;top:646px" width="30" height="30" viewBox="0 0 30 30"><circle cx="15" cy="15" r="15" fill="#fff"/><path d="M12 9l9 6-9 6z" fill="#111"/></svg>
  <p class="copy abs" style="left:360px;top:729px;width:224px">What small business owner can’t relate to theongoing task of attracting new customers? Struggling with cash flow? Or how about not having enough time in the day? It’s obvious that small businesses suffer from a lack of support. And that’s where we come in</p>
  <div class="btn abs" style="left:409px;top:828px;width:126px">WHITEBOARD VIDEO</div>

  <h3 class="col-head abs" style="left:600px;top:565px;width:218px;font-weight:400">Become an Affiliate</h3>
  <div class="affiliate-box abs" style="left:610px;top:603px;width:198px;height:115px"><span class="affiliate-mark"></span><span class="affiliate-name">Harbor Insurance</span></div>
  <p class="copy abs" style="left:610px;top:730px;width:200px">If you have a network of small businesses, let us help to create additional value for your members and make money for your network. Talk to us today about how we can help.</p>

  <div class="partners abs">
    <span class="partner">Granmore</span>
    <span class="partner">PlanDeck</span>
    <span class="partner">KVR</span>
  </div>
</main>

<footer class="footer abs">
  <div class="foot-col abs" style="left:103px;top:30px"><h4>SITE DIRECTORY</h4><ul><li>Search the Directory</li><li>Create a Directory Listing</li><li>Quote Finder</li><li>Coupns</li><li>Submit Coupon</li><li>Advertise with us</li></ul></div>
  <div class="foot-col abs" style="left:254px;top:30px"><h4>SITE DIRECTORY</h4><ul><li>Join the Forum</li><li>Submit an Article or Video</li><li>Affiliates</li><li>Become an Affiliate</li><li>Case Studies</li><li>Help Guides</li></ul></div>
  <div class="foot-col abs" style="left:401px;top:30px"><h4>POPULAR CATEGORIES</h4><ul><li>Etiam est nunc</li><li>Venenatis tristique</li><li>Emperdiet ac nisl</li><li>Cum sociis natoque</li><li>Penatibus et magnis</li></ul></div>
  <div class="foot-col abs" style="left:582px;top:30px"><h4>ABOUT</h4><ul><li>About Us</li><li>Contact Us</li><li>Term &amp; Conditions</li><li>Privacy Policy</li><li>Supporting</li><li>Sitemap</li></ul></div>
  <div class="foot-col abs" style="left:706px;top:30px"><h4>GET IN TOUCH</h4><div class="social"><i style="background:#c4302b"></i><i></i><i style="background:#3aa3e3"></i><i style="background:#2a6fb0"></i></div></div>
</footer>

<div class="legal abs"><p>© 2014 Company Name  All right reserved  Term of Use</p></div>

</body>
</html>
```